Graphic designs required for HR consulting Website

We need to items designed to be used on our website and in presentations.
Please view our website for design ideas.
http://www.brightpeak.com.au.17.morvane.pw
See attached Powerpoint doc for more info.
InfoGraphic 1
Needs to be turned into an infographic that will be embedded into the BrightPeak HR website.
The fonts should be Helvetica Neue and should have the look and feel of the website.
InfoGraphic 2
Needs to be turned into an infographic that will be embedded into the BrightPeak HR website and used in PPT and WORD proposals.
The fonts should be Helvetica Neue, the look and
feel should be consistent with the first infographic.
A mountain analogy is needed that shows how the sequence of services will come together to take businesses on the journey to becoming great.
2 versions of the same information are shown on the following slides. The first is for ease of visibility, the second is to show the sequence of services on the journey.
Samples of possible design ideas for inspiration are at bottom of ppt.

```html
<!DOCTYPE html>
<html lang="en">
<head>
<meta charset="utf-8">
<title>Infographic 1 – The Path to Greatness</title>
<link rel="stylesheet" href="https://fonts.googleapis.com/css2?family=Inter:wght@300;400&display=swap">
<style>
  :root {
    --page-bg: #ededed;
    --page-glow: #fafafa;
    --ink: #111111;
    --label: #ffffff;
    --tier-1: #000000;
    --tier-2: #02202f;
    --tier-3: #043a57;
    --tier-4: #04629a;
    --tier-5: #0a88cc;
    --tip: #2d9fdc;
  }
  html, body {
    margin: 0;
    padding: 0;
    width: 1200px;
    height: 1200px;
    overflow: hidden;
  }
  body {
    background: radial-gradient(circle at 45% 40%, var(--page-glow) 0%, var(--page-bg) 75%);
    font-family: "Inter", "Helvetica Neue", Arial, sans-serif;
  }
  .infographic {
    display: block;
    width: 1200px;
    height: 1200px;
  }
  .infographic-title {
    font-family: "Inter", "Helvetica Neue", Arial, sans-serif;
    font-weight: 300;
    font-size: 72px;
    letter-spacing: -2px;
    fill: var(--ink);
  }
  .tier-label {
    font-family: "Inter", "Helvetica Neue", Arial, sans-serif;
    font-weight: 300;
    font-size: 46px;
    letter-spacing: -1.5px;
    fill: var(--label);
    text-anchor: middle;
  }
  .tier-1 { fill: var(--tier-1); }
  .tier-2 { fill: var(--tier-2); }
  .tier-3 { fill: var(--tier-3); }
  .tier-4 { fill: var(--tier-4); }
  .tier-5 { fill: var(--tier-5); }
  .tier-tip { fill: var(--tip); }
</style>
</head>
<body>
<svg class="infographic" viewBox="0 0 1500 1500" xmlns="http://www.w3.org/2000/svg" role="img" aria-label="Five-tier cone showing the stages of greatness">
  <defs>
    <linearGradient id="ribbon-5" x1="0" x2="1"><stop offset="0" stop-color="#0588d6"/><stop offset="1" stop-color="#86d2f2"/></linearGradient>
    <linearGradient id="ribbon-4" x1="0" x2="1"><stop offset="0" stop-color="#05609a"/><stop offset="1" stop-color="#7fb8d8"/></linearGradient>
    <linearGradient id="ribbon-3" x1="0" x2="1"><stop offset="0" stop-color="#0a3f5e"/><stop offset="1" stop-color="#6896ae"/></linearGradient>
    <linearGradient id="ribbon-2" x1="0" x2="1"><stop offset="0" stop-color="#06202e"/><stop offset="1" stop-color="#506a78"/></linearGradient>
    <linearGradient id="ribbon-1" x1="0" x2="1"><stop offset="0" stop-color="#030303"/><stop offset="1" stop-color="#3a3a3a"/></linearGradient>
    <linearGradient id="cone-shine" x1="0" x2="1">
      <stop offset="0" stop-color="#ffffff" stop-opacity="0.05"/>
      <stop offset="0.15" stop-color="#ffffff" stop-opacity="0.5"/>
      <stop offset="0.55" stop-color="#ffffff" stop-opacity="0.45"/>
      <stop offset="1" stop-color="#ffffff" stop-opacity="0"/>
    </linearGradient>
    <clipPath id="cone-shape">
      <path d="M613 218 L113 1225 A498 145 0 0 0 1110 1225 Z"/>
    </clipPath>
  </defs>

  <text class="infographic-title" x="98" y="202">Infographic 1</text>

  <g class="ribbons">
    <path fill="url(#ribbon-1)" d="M620 1052 H1438 C1340 1100 1275 1160 1258 1218 H620 Z"/>
    <path fill="url(#ribbon-2)" d="M620 886 H1356 C1258 934 1193 994 1177 1052 H620 Z"/>
    <path fill="url(#ribbon-3)" d="M620 720 H1274 C1176 768 1111 828 1095 886 H620 Z"/>
    <path fill="url(#ribbon-4)" d="M620 553 H1192 C1094 601 1029 661 1013 720 H620 Z"/>
    <path fill="url(#ribbon-5)" d="M620 388 H1110 C1012 436 947 496 930 553 H620 Z"/>
  </g>

  <g class="cone">
    <path class="tier-1" d="M613 218 L113 1225 A498 145 0 0 0 1110 1225 Z"/>
    <path class="tier-2" d="M613 218 L196 1062 A416 118 0 0 0 1028 1062 Z"/>
    <path class="tier-3" d="M613 218 L280 892 A333 95 0 0 0 945 892 Z"/>
    <path class="tier-4" d="M613 218 L362 727 A250 70 0 0 0 862 727 Z"/>
    <path class="tier-5" d="M613 218 L443 562 A170 42 0 0 0 782 562 Z"/>
    <path class="tier-tip" d="M613 218 L525 396 A88 18 0 0 0 700 396 Z"/>
    <g clip-path="url(#cone-shape)">
      <path fill="url(#cone-shine)" d="M613 218 L565 1400 L945 1400 Z"/>
    </g>
  </g>

  <g class="tier-labels">
    <text class="tier-label" x="615" y="472">5. Em-</text>
    <text class="tier-label" x="617" y="519">bedding</text>
    <text class="tier-label" x="617" y="566">Greatness</text>

    <text class="tier-label" transform="rotate(-3 617 690)" x="617" y="690">4. Developing</text>
    <text class="tier-label" x="617" y="742">Greatness</text>

    <text class="tier-label" transform="rotate(-4 615 900)" x="615" y="905">3. Resourcing Greatness</text>

    <text class="tier-label" transform="rotate(-4 615 1090)" x="615" y="1095">2. The Heart of Greatness</text>

    <text class="tier-label" transform="rotate(-5 618 1240)" x="618" y="1250">1. The Foundations of Greatness</text>
    <text class="tier-label" transform="rotate(-6 625 1290)" x="625" y="1300">Trusted advice and compliance support</text>
  </g>
</svg>
</body>
</html>
```